Word Bureau Ostrelle Templates

We run a large number of businesses, including schools, airports, hotels and offices. We write reports on a daily basis and are looking for a strong and sexy WORD Template. We already have a logo in place (see graphical chart attached), that is rights' protected. We are looking for a beautiful wich reflect modern design and human aspects. Our logo has 2 design, full fill and watermark. It can be used in red or black.

Architects, Fire brigade, Building investors, contactors

• Arial, Calibri, ...

• Cover page, summary, Bullet points, Tables, Figures, Annex

```html
<!DOCTYPE html>
<html lang="en">
<head>
<meta charset="utf-8">
<title>Bureau Ostrelle – Report Template Pages</title>
<link href="https://fonts.googleapis.com/css2?family=Roboto+Condensed:wght@400;700&family=Roboto:wght@400;500&display=swap" rel="stylesheet">
<style>
:root{
  --red:#e8403f;
  --red-deep:#c41f1e;
  --red-soft:#f6b6b4;
  --pink-row:#fbe3e2;
  --grey-row:#f1f1f1;
  --ink:#333;
  --muted:#666;
  --rule:#d9d9d9;
  --stage:#0e0e0e;
  --white:#fff;
}
*{box-sizing:border-box;margin:0;padding:0}
html,body{width:866px;height:1200px;overflow:hidden}
body{background:var(--stage);position:relative;font-family:"Roboto",Arial,sans-serif;color:var(--ink)}
.page{position:absolute;width:272px;height:386px;background:var(--white);overflow:hidden}
.col-1{left:20px}.col-2{left:302px}.col-3{left:583px}
.row-1{top:11px}.row-2{top:406px}.row-3{top:798px}
.abs{position:absolute}
.brand{font-family:"Roboto",Arial,sans-serif;font-weight:500;line-height:.95;color:var(--red)}
.head-band{position:absolute;left:0;top:3px;width:100%;height:24px;background:var(--red);color:var(--white);display:flex;align-items:center;justify-content:space-between;padding:0 7px}
.head-band .title{font-family:"Roboto Condensed",Arial,sans-serif;font-size:12px;font-weight:700;letter-spacing:.2px}
.head-band .brand{color:var(--white);font-size:8px}
.foot-band{position:absolute;left:0;bottom:0;width:100%;height:14px;background:var(--red);color:var(--white);font-size:7px;display:flex;align-items:center;justify-content:space-between;padding:0 7px}
.body-copy{font-size:6.5px;line-height:1.68;text-align:justify;color:var(--ink)}
.para-title{font-family:"Roboto Condensed",Arial,sans-serif;font-weight:700;color:var(--red);font-size:10.5px}
.photo{position:absolute}
/* team */
.team-head{left:9px;top:37px;font-family:"Roboto Condensed",Arial,sans-serif;font-size:11px}
.team-intro{left:9px;top:53px;width:256px;font-size:5.8px;line-height:1.6;color:var(--ink)}
.member{position:absolute;width:118px}
.member .photo{left:0;top:0;width:75px;height:72px;background:linear-gradient(150deg,#8a7a70,#3a3230)}
.member .name{position:absolute;left:8px;top:66px;width:86px;height:13px;background:var(--red);color:var(--white);font-family:"Roboto Condensed",Arial,sans-serif;font-size:8px;font-weight:700;padding:2px 4px}
.member .role{position:absolute;left:11px;top:82px;font-size:5.5px;font-weight:500}
.member .desc{position:absolute;left:11px;top:89px;width:108px;font-size:5.3px;line-height:1.7;color:var(--muted)}
/* address page */
.address{font-size:7.6px;line-height:1.82;color:var(--ink)}
/* tables & lists */
.benefits{position:absolute;left:10px;top:68px;width:252px;border-collapse:collapse;font-size:6.8px;color:var(--muted)}
.benefits th{background:var(--red);color:var(--white);font-family:"Roboto Condensed",Arial,sans-serif;font-weight:700;font-size:8px;height:18px;text-align:left;padding:0 5px}
.benefits th:last-child{text-align:right}
.benefits td{padding:6px 5px;line-height:1.5;height:53px;vertical-align:top}
.benefits tr.grey td{background:var(--grey-row)}
.benefits tr.pink td{background:var(--pink-row)}
.toc{position:absolute;left:19px;top:56px;width:237px;list-style:none;font-size:7.6px;color:var(--ink)}
.toc li{height:25.3px;display:flex;justify-content:space-between;align-items:center;border-bottom:1px solid var(--rule)}
.toc li.plain{border-bottom:none}
.notes p{font-size:6.6px;line-height:1.6;color:var(--ink);padding:5px 0;border-bottom:1px solid var(--rule)}
</style>
</head>
<body>

<!-- Team page -->
<section class="page col-1 row-1">
  <div class="head-band"><span class="title">PROJECT TITLE HERE</span><span class="brand">Bureau<br>Ostrelle</span></div>
  <h2 class="abs team-head">OUR TEAM</h2>
  <p class="abs team-intro">since the 1500s, when an unknown printer took a galley of type and scrambled it to make a type specimen book. It has survived not only five centuries, but also the leap into electronic typesetting, remaining essentially unchanged. It was popularised in the 1960s with the release</p>
  <div class="member" style="left:12px;top:89px">
    <div class="photo" role="img" aria-label="Portrait photo of the team lead"></div>
    <div class="name">NAME HERE</div><div class="role">TEAM LEAD</div>
    <p class="desc">Morbi interdum mollis sapien. Sed ac risus. Phasellus lacinia, magna a ullamcorper laoreet, lectus arcu pulvinar risus, vitae facilisis libero dolor a purus. lacinia vel.</p>
  </div>
  <div class="member" style="left:138px;top:89px">
    <div class="photo" role="img" aria-label="Portrait photo of the expert consultant"></div>
    <div class="name">NAME HERE</div><div class="role">EXPERT CONSULTANT</div>
    <p class="desc">Morbi interdum mollis sapien. Sed ac risus. Phasellus lacinia, magna a ullamcorper laoreet, lectus arcu pulvinar risus, vitae facilisis libero dolor a purus. lacinia vel.</p>
  </div>
  <div class="member" style="left:12px;top:230px">
    <div class="photo" role="img" aria-label="Portrait photo of the communications lead" style="background:linear-gradient(150deg,#9aa0a6,#4a4e52)"></div>
    <div class="name">NAME HERE</div><div class="role">COMMUNICATIONS LEAD</div>
    <p class="desc">Morbi interdum mollis sapien. Sed ac risus. Phasellus lacinia, magna a ullamcorper laoreet, lectus arcu pulvinar risus, vitae facilisis libero dolor a purus. lacinia vel.</p>
  </div>
  <div class="member" style="left:138px;top:230px">
    <div class="photo" role="img" aria-label="Portrait photo of the analytics specialist" style="background:linear-gradient(150deg,#5a5a5a,#1e1e1e)"></div>
    <div class="name">NAME HERE</div><div class="role">ANALYTICS</div>
    <p class="desc">Morbi interdum mollis sapien. Sed ac risus. Phasellus lacinia, magna a ullamcorper laoreet, lectus arcu pulvinar risus, vitae facilisis libero dolor a purus. lacinia vel.</p>
  </div>
  <div class="foot-band"><span>www.website.com</span><span>01</span></div>
</section>

<!-- Back cover -->
<section class="page col-2 row-1">
  <svg class="abs" width="272" height="386" viewBox="0 0 272 386" style="left:0;top:0">
    <defs><linearGradient id="bc-red" x1="0" y1="0" x2="0" y2="1"><stop offset="0" stop-color="#ea4341"/><stop offset="1" stop-color="#d42c2b"/></linearGradient></defs>
    <rect width="272" height="280" fill="url(#bc-red)" role="img" aria-label="Red-tinted photo of an industrial plant skyline"/>
    <polygon points="0,222 272,262 272,386 0,386" fill="#fff"/>
    <polygon points="0,222 272,262 272,267 0,227" fill="#3a3a3a"/>
    <rect y="375" width="272" height="11" fill="var(--red)"/>
  </svg>
  <p class="abs" style="left:21px;top:33px;font-size:5px;font-weight:700;color:#fff">Paragraph Title here</p>
  <p class="abs" style="left:21px;top:43px;width:133px;font-size:3.6px;line-height:1.7;color:#fff">In the past three years, our firm has not lost any nonprofit clients. Our five largest clients lost in that timeframe are all financial institutions acquired by another company. We have not had any client retention issues related to unresolved auditing or accounting matters over this period.</p>
  <div class="abs brand" style="left:48px;top:263px;font-size:16px;color:#222">Bureau<br>Ostrelle</div>
  <div class="abs address" style="left:48px;top:300px">Adress Line Text here<br>Adress Line Text here<br>Adress Line Text here</div>
</section>

<!-- Cover -->
<section class="page col-3 row-1" style="width:275px">
  <svg class="abs" width="275" height="386" viewBox="0 0 275 386" style="left:0;top:0">
    <defs><radialGradient id="cv-red" cx=".62" cy=".35" r=".8"><stop offset="0" stop-color="#ef5a50"/><stop offset=".6" stop-color="#d8302d"/><stop offset="1" stop-color="#b81b1b"/></radialGradient></defs>
    <rect width="275" height="275" fill="url(#cv-red)" role="img" aria-label="Red-tinted photo of a welder at work with sparks"/>
    <polygon points="0,265 275,222 275,386 0,386" fill="#fff"/>
    <polygon points="0,265 275,222 275,227 0,270" fill="#3a3a3a"/>
    <rect y="375" width="275" height="11" fill="var(--red)"/>
  </svg>
  <h1 class="abs" style="right:14px;top:270px;font-family:'Roboto',sans-serif;font-weight:400;font-size:14px;color:var(--red)">Project Title Here</h1>
  <p class="abs" style="right:14px;top:289px;font-size:12px;color:#555">Subtext here</p>
  <div class="abs brand" style="right:16px;top:322px;font-size:17px;color:#222">Bureau<br>Ostrelle</div>
</section>

<!-- Text page -->
<section class="page col-1 row-2">
  <div class="head-band"><span class="title">PROJECT TITLE HERE</span><span class="brand">Bureau<br>Ostrelle</span></div>
  <h3 class="abs para-title" style="left:10px;top:37px">Paragraph Title here</h3>
  <p class="abs body-copy" style="left:10px;top:51px;width:250px">In the past three years, our firm has not lost any nonprofit clients. Our five largest clients lost in that timeframe are all financial institutions that were acquired by another company that was not an existing client of the firm. We have not had any client retention issues that related to unresolved auditing or accounting matters. In the past three years, our firm has not lost any nonprofit clients. Our five largest clients lost in that timeframe are all financial institutions that were acquired by another company that was not an existing client of the firm. We have not had any client retention issues that related to unresolved auditing or accounting matters.</p>
  <h3 class="abs para-title" style="left:10px;top:162px">Paragraph Title here</h3>
  <p class="abs body-copy" style="left:10px;top:176px;width:250px">In the past three years, our firm has not lost any nonprofit clients. Our five largest clients lost in that timeframe are all financial institutions that were acquired by another company that was not an existing client of the firm. We have not had any client retention issues that related to unresolved auditing or accounting matters. In the past three years, our firm has not lost any nonprofit clients. Our five largest clients lost in that timeframe are all financial institutions that were acquired by another company that was not an existing client of the firm. We have not had any client retention issues that related to unresolved auditing or accounting matters.</p>
  <div class="abs" style="left:10px;top:282px;width:250px;height:76px;background:var(--red);color:#fff;font-size:5.6px;line-height:1.95;padding:6px 8px">three years, our firm has not lost any nonprofit clients. Our five largest clients lost in that timeframe are all financial institutions that were acquired by another company that was not an existing client of the firm. We have not had any client retention issues that related to unresolved auditing or accounting matters. three years, our firm has not lost any nonprofit clients. Our five largest clients lost in that timeframe a</div>
  <div class="foot-band"><span>www.website.com</span></div>
  <svg class="abs" width="16" height="16" style="right:6px;bottom:1px"><circle cx="8" cy="8" r="7.5" fill="#111"/><text x="8" y="10.5" font-size="6.5" fill="#fff" text-anchor="middle" font-family="Roboto,sans-serif">01</text></svg>
</section>

<!-- Management page -->
<section class="page col-2 row-2">
  <svg class="abs" width="272" height="130" viewBox="0 0 272 130" style="left:0;top:0">
    <path d="M0 0H272V92Q150 140 0 112Z" fill="#e4504c" role="img" aria-label="Red-tinted photo of the management team"/>
  </svg>
  <h2 class="abs" style="left:17px;top:42px;font-family:'Roboto Condensed',sans-serif;font-weight:700;font-size:11px;color:#fff">OUR MANAGEMENT</h2>
  <h3 class="abs para-title" style="left:13px;top:120px">Paragraph Title here</h3>
  <p class="abs body-copy" style="left:13px;top:134px;width:247px">In the past three years, our firm has not lost any nonprofit clients. Our five largest clients lost in that timeframe are all financial institutions that were acquired by another company that was not an existing client of the firm. We have not had any client retention issues that related to unresolved auditing or accounting matters. In the past three years, our firm has not lost any nonprofit clients. Our five largest clients lost in that timeframe are all financial institutions that were acquired by another company that was not an existing client of the firm. We have not had any client retention issues that related to unresolved auditing or accounting matters.</p>
  <div class="abs" style="left:13px;top:246px;width:247px;height:13px;background:var(--red);color:#fff;font-size:7px;padding:2px 5px">Accounting matters</div>
  <div class="abs notes" style="left:13px;top:262px;width:247px">
    <p>We have not had any client retention issues that related to unresolved auditing or accounting matters.</p>
    <p>We have not had any client retention issues that related to unresolved auditing or accounting matters.</p>
    <p>We have not had any client retention issues that related to unresolved auditing or accounting matters.</p>
  </div>
  <div class="foot-band" style="height:16px"><span>www.website.com</span><span>Page : 01</span></div>
</section>

<!-- Section divider -->
<section class="page col-3 row-2" style="width:274px;background:linear-gradient(160deg,#e9403e,#e13634 60%,#d42d2c)" role="img" aria-label="Red-tinted photo of a handshake">
  <h2 class="abs" style="right:14px;top:144px;font-weight:400;font-size:19px;color:#fff">Project Title Here</h2>
  <p class="abs" style="right:16px;top:170px;font-size:15px;color:#1a1a1a">Subtext here</p>
  <div class="abs brand" style="left:155px;top:260px;font-size:17px;color:#fff">Bureau<br>Ostrelle</div>
  <p class="abs" style="left:158px;top:304px;font-size:9px;font-weight:500;color:#fff;letter-spacing:.3px">Persentator Name</p>
</section>

<!-- Benefits page -->
<section class="page col-1 row-3">
  <div class="abs brand" style="right:9px;top:8px;font-size:8.5px;color:#222">Bureau<br>Ostrelle</div>
  <h2 class="abs" style="left:10px;top:43px;font-weight:400;font-size:14px;font-family:'Roboto Condensed',sans-serif">Benefits to Our Clients</h2>
  <table class="benefits">
    <tr><th>Harwick Advantage</th><th>Benefit to Our Clients</th></tr>
    <tr class="grey"><td>Client service teams can tap into a deep pool of resources and access technical and industry experience</td><td>Client service teams can tap into a deep pool of resources and access technical and industry experience</td></tr>
    <tr class="pink"><td>Client service teams can tap into a deep pool of resources and access technical and industry experience</td><td>Client service teams can tap into a deep pool of resources and access technical and industry experience</td></tr>
    <tr class="grey"><td>Client service teams can tap into a deep pool of resources and access technical and industry experience</td><td>Client service teams can tap into a deep pool of resources and access technical and industry experience</td></tr>
  </table>
  <h3 class="abs para-title" style="left:12px;top:264px;font-weight:400;font-size:11px">Client Retention</h3>
  <p class="abs body-copy" style="left:12px;top:280px;width:248px;font-size:6.8px;text-align:left">In the past three years, our firm has not lost any nonprofit clients. Our five largest clients lost in that timeframe are all financial institutions that were acquired by another company that was not an existing client of the firm. We have not had any client retention issues that related to unresolved auditing or accounting matters.</p>
  <svg class="abs" width="272" height="16" style="left:0;bottom:0"><rect width="272" height="16" fill="var(--red)"/><polygon points="218,0 226,0 220,16 212,16" fill="#fff"/><text x="6" y="11" font-size="7" fill="#fff" font-family="Roboto,sans-serif">www.website.com</text><text x="234" y="11" font-size="6.5" fill="#fff" font-family="Roboto,sans-serif">Page : 01</text></svg>
</section>

<!-- Contents page -->
<section class="page col-2 row-3" style="left:306px;width:270px">
  <div class="abs brand" style="right:9px;top:8px;font-size:8.5px;color:#222">Bureau<br>Ostrelle</div>
  <h2 class="abs para-title" style="left:19px;top:37px;font-size:11px">Table of Contents</h2>
  <ol class="toc">
    <li><span>Firm Overview</span><span>1</span></li>
    <li><span>Nonprofit Practice Group</span><span>4</span></li>
    <li><span>Audit and Tax Services</span><span>7</span></li>
    <li><span>Use of Technology</span><span>11</span></li>
    <li><span>Ease of Transition</span><span>12</span></li>
    <li><span>Engagement Organization</span><span>14</span></li>
    <li><span>Professional Fees and Timeline</span><span>17</span></li>
    <li><span>Client References</span><span>21</span></li>
    <li class="plain"><span>Appendix</span><span></span></li>
    <li class="plain"><span>A – Peer Review Inspection</span><span>22</span></li>
  </ol>
  <svg class="abs" width="270" height="16" style="left:0;bottom:0"><rect width="270" height="16" fill="var(--red)"/><polygon points="216,0 224,0 218,16 210,16" fill="#fff"/><text x="6" y="11" font-size="7" fill="#fff" font-family="Roboto,sans-serif">www.website.com</text><text x="232" y="11" font-size="6.5" fill="#fff" font-family="Roboto,sans-serif">Page : 01</text></svg>
</section>

<!-- Figure page -->
<section class="page col-3 row-3" style="left:587px;width:271px">
  <div class="abs brand" style="right:9px;top:8px;font-size:8.5px;color:#222">Bureau<br>Ostrelle</div>
  <h3 class="abs para-title" style="left:19px;top:59px;font-size:11.5px">Paragraph title here</h3>
  <p class="abs body-copy" style="left:19px;top:76px;width:238px;font-size:6.6px;text-align:left">In the past three years, our firm has not lost any nonprofit clients. Our five largest clients lost in that timeframe are all financial institutions that were acquired by another company that was not an existing client of the firm. We have not had any client retention issues that related to unresolved auditing or accounting matters. In the past three years, our firm has not lost any nonprofit clients. Our five largest clients lost in that timeframe are all financial institutions that were acquired by another company that was not an existing client of the firm.</p>
  <svg class="abs" width="271" height="170" viewBox="0 0 271 170" style="left:0;top:180" role="img" aria-label="Three overlapping circles diagram">
    <circle cx="110" cy="54" r="49" fill="#ea4544"/>
    <circle cx="172" cy="54" r="49" fill="#f37d7b" opacity=".6"/>
    <circle cx="141" cy="114" r="49" fill="#f6a6a4" opacity=".6"/>
    <g fill="none" stroke="#fff" stroke-width="1.6">
      <rect x="81" y="42" width="20" height="17" rx="2"/><circle cx="92" cy="50.5" r="4.5"/>
      <circle cx="190" cy="51" r="9"/><path d="M190 45v6l4 3"/><path d="M182 42l-3-3M198 42l3-3"/>
      <circle cx="141" cy="135" r="7.5"/><circle cx="141" cy="135" r="2.5"/><path d="M141 124v3"/>
    </g>
  </svg>
  <svg class="abs" width="271" height="16" style="left:0;bottom:0"><rect width="271" height="16" fill="var(--red)"/><polygon points="217,0 225,0 219,16 211,16" fill="#fff"/><text x="6" y="11" font-size="7" fill="#fff" font-family="Roboto,sans-serif">www.website.com</text><text x="233" y="11" font-size="6.5" fill="#fff" font-family="Roboto,sans-serif">Page : 01</text></svg>
</section>

</body>
</html>
```